Web Design Project

We are an online tax Continuing education provider. We provide online courses for tax preparers. We want the front end page to be user friendly and for the buyer to know exactly what they are looking at. We want a front end page to look smiliar www.marblequill.com. It should have a similar feel to this one.
Our website address will be www.7382LQ.com
We currently have another website that is www.LedgerNoks.com but we do not want it to look like this. We want a different look but same information.
We have a logo already which is attached. We don't have specific colors in mind for the front page but don't want it to be too busy looking. It should stand out but not too simple either.
Target Market(s)
Tax Preparers. More serious and professional but these folks are usually not tech savy. Simple, easy to use, and functional is key.
Industry/Entity Type
Education
Requirements
Must have
- Use standard HTML & CSS. NO other coding is needed.
We are looking for 5-7 pages including Home page, log in, FAQ.
Please look at our current website www.LedgerNoks.com and also www.marblequill.com

```html
<!DOCTYPE html>
<html lang="en">
<head>
<meta charset="utf-8">
<title>7382 LQ – Continuing Education Made Simple</title>
<link rel="stylesheet" href="https://fonts.googleapis.com/css2?family=Arimo:ital,wght@0,400;0,700;1,400&family=Oswald:wght@500&display=swap">
<style>
:root{
  --ink:#222;
  --navy:#1b5a7e;
  --grey-text:#8a8a8a;
  --red:#c0171a;
  --green:#bcd232;
  --blue:#4fcfea;
  --orange:#f58c1d;
  --panel:#f5f5f5;
  --line:#cfcfcf;
  --footer:#5a5a5a;
  --btn-rim:#7a4a1c;
  --bulletin:#9ccd2a;
}
*{box-sizing:border-box;margin:0;padding:0}
html,body{width:1200px;height:1160px;overflow:hidden}
body{position:relative;background:#fff;font-family:"Arimo",Arial,sans-serif;color:var(--ink)}
.header{position:absolute;left:0;top:0;width:1200px;height:96px;background:linear-gradient(#f7f7f7,#e6e6e6);border-bottom:2px solid #d2d2d2}
.brand{position:absolute;left:222px;top:32px;display:flex;align-items:center;gap:8px;font-size:24px;font-weight:700;color:var(--navy)}
.brand-dot{width:22px;height:22px;border-radius:50%;background:var(--green)}
.nav{position:absolute;top:32px;left:505px;display:flex}
.nav a{width:96px;height:32px;line-height:32px;text-align:center;font-size:12px;font-weight:700;color:#666;text-decoration:none}
.nav a.active{background:linear-gradient(#6a6a6a,#2e2e2e);color:#fff;border-radius:6px;box-shadow:0 2px 3px rgba(0,0,0,.35)}
.hero{position:absolute;left:216px;top:122px;width:768px;height:230px;border:1px solid #e2e2e2;overflow:hidden;background:#fff}
.hero-photo{position:absolute;right:0;top:0;width:420px;height:230px;background:linear-gradient(90deg,#fff 0%,#e9ecef 25%,#c9a98a 60%,#8a6b52 100%)}
.hero-title{position:absolute;left:38px;top:52px;font-size:35px;line-height:36px;font-weight:700;color:var(--navy)}
.hero-sub{position:absolute;left:38px;top:128px;font-size:19px;font-weight:700;color:var(--grey-text)}
.hero-sub em{font-style:italic}
.hero-points{position:absolute;left:38px;top:158px;display:flex;gap:12px;font-size:15px;font-weight:700;color:var(--red)}
.hero-points span{display:flex;align-items:center;gap:7px}
.dots{position:absolute;left:38px;top:208px;display:flex;gap:3px}
.dots i{width:7px;height:7px;border-radius:50%;background:#d4d4d4}
.dots i:first-child{background:#1ea0dc}
.package{position:absolute;top:376px;width:240px;height:352px;border-radius:6px;color:#222;padding:12px 16px}
.package h2{text-align:center;color:#fff;font-size:14.5px;font-weight:700;margin-bottom:6px}
.package p,.package li{font-size:10.3px;line-height:17.6px;white-space:nowrap}
.package ul{list-style:none}
.package li{position:relative;padding-left:16px}
.package li svg{position:absolute;left:1px;top:4px}
.pkg-ce{left:216px;background:var(--green)}
.pkg-rtrp{left:480px;background:var(--blue)}
.pkg-combo{left:744px;background:var(--orange)}
.indent{padding-left:23px}
.more{position:absolute;left:16px;top:266px;color:#fff;font-size:10.5px;font-weight:700}
.register{position:absolute;left:36px;top:298px;width:168px;height:34px;border-radius:17px;background:var(--btn-rim);padding:3px}
.register span{display:flex;align-items:center;justify-content:center;gap:28px;height:28px;border-radius:14px;background:linear-gradient(#ee5a1c,#c22a08);color:#fff;font-size:12.5px;font-weight:700}
.register b{width:14px;height:14px;border-radius:50%;background:#2b2b2b;display:inline-block;position:relative}
.register b::after{content:"";position:absolute;left:5px;top:4px;border-left:5px solid #fff;border-top:3px solid transparent;border-bottom:3px solid transparent}
.info{position:absolute;left:216px;top:752px;width:768px;height:80px;background:var(--panel);border:1px solid var(--line)}
.info-text{position:absolute;left:14px;top:21px;font-size:16px;font-weight:700;color:#888;line-height:18px}
.bulletin{position:absolute;left:385px;top:19px;width:366px;height:40px;background:linear-gradient(#bde04a,var(--bulletin));border:1px solid #8ab722;border-radius:3px;text-align:center;line-height:38px;font-family:"Oswald",Arial,sans-serif;font-size:18px;color:#6f8c16}
.provider{position:absolute;top:856px;width:240px;height:88px;border:1px solid var(--line);background:#fff}
.provider p{position:absolute;left:16px;top:18px;font-size:11.5px;line-height:17.6px}
.provider .art{position:absolute;right:20px;top:10px;width:60px;height:66px;border-radius:3px}
.pv1{left:216px}.pv2{left:480px}.pv3{left:744px}
.pv1 .art{background:#1f5fae;border-radius:8px;width:50px;right:22px}
.pv2 .art{background:linear-gradient(135deg,#fbf3cc,#e6cf7e)}
.pv3 .art{background:linear-gradient(135deg,#f8f1d0,#d9c276);width:76px;right:12px}
.quote{position:absolute;left:216px;top:968px;width:768px;height:80px;background:var(--panel);border:1px solid var(--line);text-align:center;padding-top:8px;font-size:19.5px;line-height:22px;font-style:italic}
.quote strong{font-style:normal}
.quote-next{position:absolute;right:-1px;bottom:-1px;width:24px;height:24px;background:#a0a0a0}
.footer{position:absolute;left:0;top:1072px;width:1200px;height:88px;background:var(--footer)}
.accreditor{position:absolute;left:216px;top:20px;width:173px;height:40px;background:#fff;display:flex;align-items:center;gap:6px;padding-left:4px;font-size:10px;line-height:12px;color:#8a8a8a}
.accreditor i{width:34px;height:32px;background:#9a9478}
.seal{position:absolute;left:400px;top:20px;width:72px;height:40px;background:#7b3b12;border:2px solid #e8a032}
.legal{position:absolute;right:216px;top:28px;font-size:10.5px;color:#fff}
.follow{position:absolute;right:216px;top:49px;display:flex;align-items:center;gap:5px;font-size:10.5px;color:#fff}
.follow i{width:22px;height:22px;border-radius:3px;margin-left:2px}
</style>
</head>
<body>
<header class="header">
  <div class="brand"><span class="brand-dot"></span>7382 LQ</div>
  <nav class="nav">
    <a class="active" href="#">Home</a><a href="#">Courses</a><a href="#">FAQs</a><a href="#">Contact</a><a href="#">Sign in</a>
  </nav>
</header>

<section class="hero">
  <div class="hero-photo" role="img" aria-label="Smiling student studying at a laptop"></div>
  <h1 class="hero-title">Continuing Education<br>Made Simple</h1>
  <p class="hero-sub">Completely Online! <em>“self-paced”</em></p>
  <div class="hero-points">
    <span><svg width="22" height="22" viewBox="0 0 22 22"><circle cx="11" cy="11" r="10" fill="#29a8e6" stroke="#d9e8f2" stroke-width="2"/><path d="M6 11l3.5 3.5L16 8" stroke="#fff" stroke-width="2.5" fill="none"/></svg>FAST</span>
    <span><svg width="22" height="22" viewBox="0 0 22 22"><circle cx="11" cy="11" r="10" fill="#29a8e6" stroke="#d9e8f2" stroke-width="2"/><path d="M6 11l3.5 3.5L16 8" stroke="#fff" stroke-width="2.5" fill="none"/></svg>EASY</span>
    <span><svg width="22" height="22" viewBox="0 0 22 22"><circle cx="11" cy="11" r="10" fill="#29a8e6" stroke="#d9e8f2" stroke-width="2"/><path d="M6 11l3.5 3.5L16 8" stroke="#fff" stroke-width="2.5" fill="none"/></svg>LOW-COST</span>
  </div>
  <div class="dots"><i></i><i></i><i></i><i></i></div>
</section>

<article class="package pkg-ce">
  <h2>15-Hour CE Package</h2>
  <p>15-Hour package for FRB Registered<br>Tax-Preparer Continuing Education:</p>
  <p>&nbsp;</p>
  <p>This package meets the following FRB<br>requirements for registered tax-preparer<br>continuing education:</p>
  <p>&nbsp;</p>
  <p>15-hour per year (beginning in calendar year<br>2013)</p>
  <p class="indent">2 hours of ethics</p>
  <p class="indent">3 hours of federal tax law updates</p>
  <p class="indent">10 hours of other federal tax law.</p>
  <span class="more">READ MORE</span>
  <a class="register"><span>Register Now! <b></b></span></a>
</article>

<article class="package pkg-rtrp">
  <h2>RTRP Test Simulator Package</h2>
  <p>Test Simulator Course Details</p>
  <ul>
    <li><svg width="11" height="9"><path d="M1 4.5l3 3L10 1" stroke="#fff" stroke-width="2.2" fill="none"/></svg>10-HR RTRP Exam Simulator Course</li>
    <li><svg width="11" height="9"><path d="M1 4.5l3 3L10 1" stroke="#fff" stroke-width="2.2" fill="none"/></svg>Study for the RTRP exam and receive</li>
    <li><svg width="11" height="9"><path d="M1 4.5l3 3L10 1" stroke="#fff" stroke-width="2.2" fill="none"/></svg>CE credit at the same time.</li>
    <li><svg width="11" height="9"><path d="M1 4.5l3 3L10 1" stroke="#fff" stroke-width="2.2" fill="none"/></svg>It is comprised of four full-length practice<br>exams (120 questions each).</li>
    <li><svg width="11" height="9"><path d="M1 4.5l3 3L10 1" stroke="#fff" stroke-width="2.2" fill="none"/></svg>The main objective of this course is to<br>give the tax preparer a crash course in<br>taking the RTRP exam.</li>
    <li><svg width="11" height="9"><path d="M1 4.5l3 3L10 1" stroke="#fff" stroke-width="2.2" fill="none"/></svg>The fourth exam attempts to mimic the<br>actual FRB exam.</li>
    <li><svg width="11" height="9"><path d="M1 4.5l3 3L10 1" stroke="#fff" stroke-width="2.2" fill="none"/></svg>Complete Study Guide covering all 7 FRB<br>test domains ( subject areas)</li>
  </ul>
  <span class="more">READ MORE</span>
  <a class="register"><span>Register Now! <b></b></span></a>
</article>

<article class="package pkg-combo">
  <h2>Combo Package</h2>
  <p>Test Simulator Course Details</p>
  <ul>
    <li><svg width="11" height="9"><path d="M1 4.5l3 3L10 1" stroke="#fff" stroke-width="2.2" fill="none"/></svg>10-HR RTRP Exam Simulator Course</li>
    <li><svg width="11" height="9"><path d="M1 4.5l3 3L10 1" stroke="#fff" stroke-width="2.2" fill="none"/></svg>Study for the RTRP exam and receive</li>
    <li><svg width="11" height="9"><path d="M1 4.5l3 3L10 1" stroke="#fff" stroke-width="2.2" fill="none"/></svg>CE credit at the same time.</li>
    <li><svg width="11" height="9"><path d="M1 4.5l3 3L10 1" stroke="#fff" stroke-width="2.2" fill="none"/></svg>It is comprised of four full-length practice<br>exams (120 questions each).</li>
    <li><svg width="11" height="9"><path d="M1 4.5l3 3L10 1" stroke="#fff" stroke-width="2.2" fill="none"/></svg>The main objective of this course is to<br>give the tax preparer a crash course in<br>taking the RTRP exam.</li>
    <li><svg width="11" height="9"><path d="M1 4.5l3 3L10 1" stroke="#fff" stroke-width="2.2" fill="none"/></svg>The fourth exam attempts to mimic the<br>actual FRB exam.</li>
    <li><svg width="11" height="9"><path d="M1 4.5l3 3L10 1" stroke="#fff" stroke-width="2.2" fill="none"/></svg>Complete Study Guide covering all 7 FRB<br>test domains ( subject areas)</li>
  </ul>
  <span class="more">READ MORE</span>
  <a class="register"><span>Register Now! <b></b></span></a>
</article>

<section class="info">
  <p class="info-text">FRB Latest Information Link<br>( Click button to open FRB document or link)</p>
  <a class="bulletin">RTRP TEST CANDIDATE INFORMATION BULLETIN</a>
</section>

<a class="provider pv1"><p>Click here to see our<br>approved provider link at<br>FRB website</p><span class="art" role="img" aria-label="Agency badge"></span></a>
<a class="provider pv2"><p>Click here to see our<br>approved provider link at<br>FRB website</p><span class="art" role="img" aria-label="Certificate with ribbon seal"></span></a>
<a class="provider pv3"><p>Click here to see our<br>approved provider link at<br>FRB website</p><span class="art" role="img" aria-label="Framed certificate with award rosette"></span></a>

<blockquote class="quote">“The courses are easy to understand, especially considering the complexity of the<br>U.S. tax codes. The pricing is very reasonable as well.” <strong>-Dana.NY</strong>
  <span class="quote-next"><svg width="24" height="24"><path d="M9 6l6 6-6 6" stroke="#fff" stroke-width="2.5" fill="none"/></svg></span>
</blockquote>

<footer class="footer">
  <div class="accreditor"><i role="img" aria-label="Accreditation badge"></i>APPROVED<br>CONTINUING EDUCATION<br>ACCREDITOR</div>
  <div class="seal" role="img" aria-label="Secure site badge"></div>
  <p class="legal">© 2013. All rights reserved. Privacy Policy. Terms of use.</p>
  <div class="follow">Follow us on <i style="background:#3b5b9a"></i><i style="background:#c9302c"></i><i style="background:#1c7bb4"></i><i style="background:#f07b22"></i></div>
</footer>
</body>
</html>
```